High-end Oceanfront Real Estate Group Needs Clean, Modern Web Design

I’m looking for a clean, professional, modern and beautiful homepage web design for a Real Estate group in Southern California, USA.

The group/company is “Marlow on the Shore,” and they specialize in high end (i.e. expensive), oceanfront real estate in the Orange County area.

The look and feel of the page should accentuate the brand qualities: luxurious/expensive, professional, and beautiful (Orange County is one of the most beautiful areas in all the US and we would love the site to emphasize the beautiful beaches and scenery it has to offer).

Looks we like:
• www.brantleyhomesrealty.example
• www.keptbyfenwick.example -- I think the design is pretty out-dated in this site, but I like the organization/layout of the site

Header Tags (I don’t know if we can fit all of these, may need a side-menu, but I’d prefer header title only if possible):
• Welcome
• Featured Listings
• Previously Sold
• Sell
• Property Search
• Team
• Videos
• Blog
• Explore O.C.
• Contact

I have attached the beach and logo pics that we would like to use as the header, a few pictures of the team, and one sample home/view pic which can be used in any of the other sections (for pictures of the homes, just find expensive oceanfront houses and that will be fine).

I promise to provide feedback to each and every design submission. I appreciate the hard work that all of you are putting into your designs. There can be only one contest winner, but I hope to give all of you helpful feedback to submit the best designs possible!

Target Market(s)

Very wealthy home owners of oceanfront properties. These properties are worth several millions of dollars, and thus the site and brand needs to be targeted to very wealthy, successful individuals and families (both US and international buyers).

Industry/Entity Type

Real Estate

Number of Pages Required

2 page

Requirements
Must have
• I don’t want to give too many requirements, because I want to let you all be creative. However, here are the few Must Haves:
• Must submit 2 page designs (a home page and a sub page)
• Must use logo provided
• Focus is mostly on homes, but I would like to include some beach/ocean imagery as well
• The first “item” on the home page should be an accordion/slider which shows pictures of homes and with 1 line of text: “List with the Leader” and two link buttons: “Sell Your Home” and “Buy Your Home”
• Color palette needs to be mainly blues--to match ocean and sky blue
• Exported in all major formats (psd,ai,eps,png,jpeg,etc)
Nice to have
• We don’t necessarily need all of these, but would like to feature most:
• List of videos
• “Meet the Team”—brief team bios and pics
• Link(s) to Blog
• “List with the Leader” – section on why they should choose this firm
• Featured Listings
• Previously Sold

```html
<!DOCTYPE html>
<html lang="en">
<head>
<meta charset="utf-8">
<title>Marlow on the Shore — Oceanfront Homes</title>
<link href="https://fonts.googleapis.com/css2?family=Open+Sans:wght@300;400;600&display=swap" rel="stylesheet">
<style>
:root{
  --blue:#2b86df;
  --blue-team:#3d95f0;
  --blue-team-alt:#378de6;
  --blue-video:#2a73b6;
  --panel:#c4d7ef;
  --page:#efefef;
  --ink:#2b2b2b;
  --muted:#6d6d6d;
  --red:#b3262b;
  --footer:#3b3e43;
  --footer-low:#303337;
  --white:#ffffff;
}
*{box-sizing:border-box;margin:0;padding:0}
html,body{width:1200px;height:3177px;overflow:hidden}
body{font-family:"Open Sans",Arial,sans-serif;background:var(--page);color:var(--ink);position:relative}
.abs{position:absolute}

/* hero */
.hero{left:0;top:0;width:1200px;height:538px;background:linear-gradient(180deg,#8fb7d8 0%,#a9c6dc 18%,#5f8a5a 34%,#4e7a3e 55%,#8a9a6b 78%,#c9c4b1 100%)}
.brand{left:183px;top:29px;color:var(--white);font-weight:300;font-size:13px;line-height:16px;letter-spacing:.5px;text-transform:uppercase;white-space:nowrap}
.nav{left:347px;top:26px;display:flex;gap:13px;font-size:10.5px;color:var(--white);text-transform:uppercase;white-space:nowrap}
.nav a{color:inherit;text-decoration:none;padding-bottom:4px}
.nav a.active{border-bottom:1px solid var(--white)}
.hero-title{left:0;top:344px;width:1200px;text-align:center;font-size:26px;letter-spacing:2px;color:#1f2b1d;font-weight:400}

/* section titles */
.section-title{left:0;width:1200px;text-align:center;font-size:28px;font-weight:400;letter-spacing:2px;color:var(--ink)}
.section-title::after{content:"";display:block;width:48px;height:3px;background:var(--blue);margin:14px auto 0}

/* list with the leader */
.leader-photo{left:166px;top:623px;width:438px;height:301px;background:linear-gradient(180deg,#6aa6e0 0%,#a9cdee 40%,#6f8d53 70%,#4f7a32 100%)}
.btn{position:absolute;top:729px;height:42px;line-height:42px;text-align:center;font-size:12px;text-transform:uppercase;letter-spacing:1px}
.btn-sell{left:227px;width:144px;background:var(--blue);color:var(--white)}
.btn-buy{left:383px;width:152px;background:var(--white);color:var(--blue)}
.why{left:604px;top:623px;width:430px;height:301px;background:var(--panel);padding:40px 22px}
.why h3{font-size:17px;font-weight:400;letter-spacing:1px;color:var(--ink)}
.why h3::after{content:"";display:block;width:48px;height:2px;background:var(--ink);margin-top:10px}
.why ul{list-style:none;margin-top:20px}
.why li{font-size:11.5px;line-height:17px;color:var(--muted);padding-left:24px;position:relative;margin-bottom:14px}
.why li::before{content:"";position:absolute;left:4px;top:5px;width:7px;height:7px;border-radius:50%;background:var(--blue)}
.why .more{display:inline-block;border:1px solid var(--ink);font-size:11px;padding:4px 10px;text-transform:uppercase;margin-top:-2px}

/* featured listings */
.beach{left:0;top:1034px;width:1200px;height:604px;background:linear-gradient(170deg,#3a6a73 0%,#5f8b8f 18%,#b7a88a 40%,#9c8462 62%,#b9a98c 80%,#cfc6b7 100%)}
.pager{left:985px;top:1070px;display:flex;gap:3px}
.pager span{width:16px;height:16px;background:var(--blue);border-radius:2px;display:flex;align-items:center;justify-content:center}
.listing{position:absolute;width:200px;height:220px;background:var(--white)}
.listing .photo{height:150px;position:relative}
.listing .price{position:absolute;right:0;bottom:8px;background:var(--white);font-size:13px;padding:3px 8px;color:var(--ink)}
.listing .addr{font-size:12px;line-height:15px;color:var(--red);padding:6px 8px 0;text-transform:uppercase;height:38px;white-space:nowrap}
.listing .meta{font-size:10px;color:var(--muted);padding:6px 8px 0;display:flex;gap:10px;align-items:center;white-space:nowrap}

/* team */
.team{left:0;top:1772px;width:1200px;height:305px;display:flex}
.member{flex:1;background:var(--blue-team);position:relative}
.member:nth-child(2){background:var(--blue-team-alt)}
.member .portrait{position:absolute;left:98px;top:61px;width:205px;height:181px;border:3px solid var(--white)}
.member .name{position:absolute;left:0;top:248px;width:100%;text-align:center;font-size:15px;color:#1d2d40;text-transform:uppercase}
.member .name::after{content:"";display:block;width:110px;height:1px;background:rgba(255,255,255,.45);margin:6px auto 0}

/* previously sold */
.sold{left:0;top:2200px;width:1200px;height:188px;display:flex}
.sold-item{flex:1;position:relative}
.sold-item .label{position:absolute;right:8px;bottom:22px;background:var(--white);font-size:13px;text-transform:uppercase;letter-spacing:1px;padding:5px 12px;color:var(--ink);white-space:nowrap}

/* videos */
.videos{left:0;top:2510px;width:1200px;height:374px;background:var(--blue-video)}
.video{left:379px;top:2542px;width:440px;height:256px;background:linear-gradient(180deg,#5a8fb8 0%,#c9b89c 45%,#4c6d3c 75%,#4f9bb0 100%)}
.play{left:570px;top:2652px}
.show-more{left:538px;top:2838px;width:122px;height:40px;border:1px solid var(--white);color:var(--white);font-size:14px;text-align:center;line-height:38px;text-transform:uppercase;letter-spacing:1px}

/* footer */
.footer{left:0;top:2884px;width:1200px;height:247px;background:var(--footer);color:#cfd1d4}
.col{position:absolute;top:28px}
.col h4{font-size:12px;font-weight:600;color:var(--white);text-transform:uppercase;letter-spacing:.5px}
.col h4::after{content:"";display:block;width:34px;height:2px;background:var(--white);margin-top:6px}
.col p{font-size:11px;line-height:15px;margin-top:12px;color:#bfc2c6;width:178px}
.post{display:flex;gap:8px;margin-top:12px;width:200px}
.post:first-of-type{margin-top:14px}
.post .thumb{flex:none;width:46px;height:36px;background:linear-gradient(180deg,#7d9fb8,#6f7f4f)}
.post .t{font-size:10.5px;line-height:13px;color:#d6d8db}
.post .d{font-size:9px;color:#8f9398;margin-top:2px}
.field{width:186px;height:28px;background:#55595f;margin-top:8px;font-size:10px;color:#9a9ea3;padding:7px 8px}
.field.first{margin-top:14px}
.field.msg{height:52px}
.submit{margin:6px 0 0 126px;width:60px;height:20px;background:var(--blue);color:var(--white);font-size:10px;text-align:center;line-height:20px;text-transform:uppercase}
.info{list-style:none;margin-top:12px}
.info li{font-size:11px;line-height:15px;color:#cfd1d4;display:flex;gap:12px;margin-bottom:9px}
.social{display:flex;gap:6px;margin-top:18px}
.social span{width:24px;height:24px;border:1px solid #8e9297;border-radius:50%}
.bottom{left:0;top:3131px;width:1200px;height:46px;background:var(--footer-low);color:#bfc2c6;font-size:11px}
.bottom .copy{position:absolute;left:183px;top:15px;display:flex;gap:6px;align-items:center}
</style>
</head>
<body>

<header>
  <div class="hero abs" role="img" aria-label="Coastal resort terrace with white pergolas, palm trees, lawns and ocean view"></div>
  <div class="brand abs">Marlow on the Shore</div>
  <nav class="nav abs">
    <a class="active">Welcome</a><a>Featured Listings</a><a>Previously Sold</a><a>Sell</a><a>Property Search</a><a>Team</a><a>Videos</a><a>Blog</a><a>Explore O.C.</a><a>Contact</a>
  </nav>
  <h1 class="hero-title abs">CELEBRATING YEARS OF EXCELLENCE</h1>
</header>

<h2 class="section-title abs" style="top:562px">LIST WITH THE LEADER</h2>
<div class="leader-photo abs" role="img" aria-label="Family home with green lawn under a blue sky"></div>
<a class="btn btn-sell">Sell Your Home</a>
<a class="btn btn-buy">Buy Your Home</a>
<div class="why abs">
  <h3>WHY CHOOSE US</h3>
  <ul>
    <li>Our agents know every cove and cliff on this coast, and we guide each sale with care from start to finish.</li>
    <li>We market each home to buyers here and abroad, with film, print and private showings that set it apart.</li>
    <li>From first visit to closing day, one team stays with you and keeps every step clear and calm.</li>
  </ul>
  <span class="more">Read More</span>
</div>

<h2 class="section-title abs" style="top:955px">FEATURED LISTINGS</h2>
<div class="beach abs" role="img" aria-label="Sandy beach with ocean waves washing ashore"></div>
<div class="pager abs">
  <span><svg width="8" height="8" viewBox="0 0 8 8"><path d="M5.5 1 2.5 4l3 3" stroke="#fff" stroke-width="1.4" fill="none"/></svg></span>
  <span><svg width="8" height="8" viewBox="0 0 8 8"><path d="M2.5 1 5.5 4l-3 3" stroke="#fff" stroke-width="1.4" fill="none"/></svg></span>
</div>

<section class="listings">
  <div class="listing" style="left:171px;top:1107px">
    <div class="photo" role="img" aria-label="Mediterranean villa at dusk" style="background:linear-gradient(180deg,#4e7fb2,#c7b38d 60%,#6a7b52)"><span class="price">$35,000,000</span></div>
    <div class="addr">1129 Harbor Crest Road,<br>CA 90200</div>
    <div class="meta"><span>Area: 10,200 Sq Ft</span><span>Bed: 3</span><span>Bath: 2</span></div>
  </div>
  <div class="listing" style="left:392px;top:1107px">
    <div class="photo" role="img" aria-label="Modern terrace with pool and ocean view" style="background:linear-gradient(180deg,#6fa5d6,#9ec1d8 50%,#7d6a55)"><span class="price">$21,450,000</span></div>
    <div class="addr">1435 Dune Lark Drive,<br>CA 90210</div>
    <div class="meta"><span>Area: 6,350 Sq Ft</span><span>Bed: 4</span><span>Bath: 3</span></div>
  </div>
  <div class="listing" style="left:613px;top:1107px">
    <div class="photo" role="img" aria-label="White modern house with swimming pool" style="background:linear-gradient(180deg,#8bb8e0,#e4e6e4 50%,#4c8fb2)"><span class="price">$28,300,000</span></div>
    <div class="addr">9555 Sea Pine Road,<br>CA 90200</div>
    <div class="meta"><span>Area: 8,200 Sq Ft</span><span>Bed: 7</span><span>Bath: 4</span></div>
  </div>
  <div class="listing" style="left:834px;top:1107px">
    <div class="photo" role="img" aria-label="Large estate lit at twilight" style="background:linear-gradient(180deg,#2d4a7a,#9a7a55 55%,#4f5f3d)"><span class="price">$23,900,000</span></div>
    <div class="addr">450 Tidewater Place,<br>CA 90210</div>
    <div class="meta"><span>Area: 7,300 Sq Ft</span><span>Bed: 6</span><span>Bath: 4</span></div>
  </div>
  <div class="listing" style="left:171px;top:1347px">
    <div class="photo" role="img" aria-label="Bright living room opening to a garden" style="background:linear-gradient(180deg,#b8c48f,#d5cbb2 55%,#8a6d4e)"><span class="price">$34,000,000</span></div>
    <div class="addr">9904 Kelp Drive,<br>CA 90210</div>
    <div class="meta"><span>Area: 9,700 Sq Ft</span><span>Bed: 4</span><span>Bath: 2</span></div>
  </div>
  <div class="listing" style="left:392px;top:1347px">
    <div class="photo" role="img" aria-label="Warm lounge with hillside view" style="background:linear-gradient(180deg,#6b5a46,#a88e6b 55%,#4d3b2e)"><span class="price">$22,650,000</span></div>
    <div class="addr">9945 Cove Ridge Drive,<br>CA 90210</div>
    <div class="meta"><span>Area: 7,150 Sq Ft</span><span>Bed: 5</span><span>Bath: 3</span></div>
  </div>
  <div class="listing" style="left:613px;top:1347px">
    <div class="photo" role="img" aria-label="Living room with wide ocean windows" style="background:linear-gradient(180deg,#6fa3cc,#d9dde0 55%,#8f8576)"><span class="price">$29,300,000</span></div>
    <div class="addr">1129 Harbor Crest Road,<br>CA 90200</div>
    <div class="meta"><span>Area: 8,700 Sq Ft</span><span>Bed: 7</span><span>Bath: 5</span></div>
  </div>
  <div class="listing" style="left:834px;top:1347px">
    <div class="photo" role="img" aria-label="Classic dining room in warm tones" style="background:linear-gradient(180deg,#c9a46e,#a27747 55%,#6b4a2e)"><span class="price">$23,900,000</span></div>
    <div class="addr">726 North Sandpiper Drive,<br>CA 90210</div>
    <div class="meta"><span>Area: 6,500 Sq Ft</span><span>Bed: 4</span><span>Bath: 3</span></div>
  </div>
</section>

<h2 class="section-title abs" style="top:1678px">OUR TEAM</h2>
<section class="team abs">
  <div class="member"><div class="portrait" role="img" aria-label="Portrait of team member Reid" style="background:linear-gradient(180deg,#8a7a66,#9fa7b2)"></div><div class="name">Reid</div></div>
  <div class="member"><div class="portrait" role="img" aria-label="Portrait of team member Clara" style="background:linear-gradient(180deg,#b9c9d6,#d8c7a8)"></div><div class="name">Clara</div></div>
  <div class="member"><div class="portrait" role="img" aria-label="Portrait of team member Nadia" style="background:linear-gradient(180deg,#6b5a4a,#2e2a2a)"></div><div class="name">Nadia</div></div>
</section>

<h2 class="section-title abs" style="top:2108px">PREVIOUSLY SOLD</h2>
<section class="sold abs">
  <div class="sold-item" role="img" aria-label="Villa with pool at sunset" style="background:linear-gradient(180deg,#c9b59c,#8c7a5f 50%,#4f7a5a)"><span class="label">Elegant Villa</span></div>
  <div class="sold-item" role="img" aria-label="Red-roofed estate among gardens" style="background:linear-gradient(180deg,#6f8fb5,#9a5a3f 45%,#4c6b34)"><span class="label">Exquisite Seacliff Retreat</span></div>
  <div class="sold-item" role="img" aria-label="White veranda overlooking the sea" style="background:linear-gradient(180deg,#7ea8cf,#e6e6e4 50%,#9d9d94)"><span class="label">Hidden Treasure</span></div>
  <div class="sold-item" role="img" aria-label="White manor on a green lawn" style="background:linear-gradient(180deg,#4f8ed0,#b8cfe0 40%,#5d8a3a)"><span class="label">Harbor View Manor</span></div>
</section>

<h2 class="section-title abs" style="top:2424px">OUR VIDEOS</h2>
<section class="videos abs"></section>
<div class="video abs" role="img" aria-label="Aerial view of a hillside mansion with pool and palms"></div>
<svg class="play abs" width="58" height="40" viewBox="0 0 58 40"><rect width="58" height="40" rx="6" fill="#1e1e1e" fill-opacity=".75"/><path d="M23 12v16l13-8z" fill="#fff"/></svg>
<div class="show-more abs">Show More</div>

<footer class="footer abs">
  <div class="col" style="left:183px">
    <h4>About Us</h4>
    <p>We help families buy and sell fine homes along the Orange County coast. Our team brings years of local knowledge, honest advice and quiet care to every move.</p>
  </div>
  <div class="col" style="left:403px">
    <h4>Recent Blog Posts</h4>
    <div class="post"><div class="thumb" role="img" aria-label="Coastal home thumbnail"></div><div><div class="t">Spring tides and new coastal listings</div><div class="d">Mar 02, 2015</div></div></div>
    <div class="post"><div class="thumb" role="img" aria-label="Living room thumbnail"></div><div><div class="t">How to stage a home with a view</div><div class="d">Feb 26, 2015</div></div></div>
    <div class="post"><div class="thumb" role="img" aria-label="Beach path thumbnail"></div><div><div class="t">A quiet guide to Laguna beach walks</div><div class="d">Feb 20, 2015</div></div></div>
  </div>
  <div class="col" style="left:618px">
    <h4>Quick Contact</h4>
    <div class="field first">Name...</div>
    <div class="field">Email...</div>
    <div class="field msg">Message...</div>
    <div class="submit">Submit</div>
  </div>
  <div class="col" style="left:836px">
    <h4>Contact Info</h4>
    <ul class="info">
      <li><svg width="10" height="14" viewBox="0 0 10 14"><path d="M5 0a5 5 0 0 1 5 5c0 4-5 9-5 9S0 9 0 5a5 5 0 0 1 5-5z" fill="#fff"/><circle cx="5" cy="5" r="2" fill="#3b3e43"/></svg><span>Southern California,<br>USA</span></li>
      <li><svg width="10" height="12" viewBox="0 0 10 12"><path d="M2 0h3l1 3-2 1c.6 1.6 1.4 2.6 3 3.4L8 6l2 1v3c-5 1-10-4-10-9z" fill="#fff"/></svg><span>555-014-2290</span></li>
      <li><svg width="12" height="10" viewBox="0 0 12 10"><rect width="12" height="10" fill="#fff"/><path d="M0 0l6 5 6-5" stroke="#3b3e43" fill="none"/></svg><span>info@marlowshore.example</span></li>
    </ul>
    <div class="social"><span></span><span></span><span></span><span></span><span></span></div>
  </div>
</footer>
<div class="bottom abs">
  <div class="copy"><svg width="12" height="12" viewBox="0 0 12 12"><circle cx="6" cy="6" r="5.3" stroke="#bfc2c6" fill="none"/><path d="M7.8 4.4A2.2 2.2 0 1 0 7.8 7.6" stroke="#bfc2c6" fill="none"/></svg>Copyright information here</div>
</div>

</body>
</html>
```